Packaging Design job - Health Supplement

We need a packaging design theme for a health supplement for Moroccan consumers. Our product is called 'Velomira'. https://norvabien.com/nos-produits/digestion/velo-mira/

It is a unique solution of three plants with recognized benefits. The activated carbon in the product allows, like plants, reduce effectively the problems related to digestion. The product is particularly effective for soothing bloating and optimizing intestinal transit as well as digestion.

We would like to see clean, modern and fresh designs.
This should give the impression of professional products of pharmaceutical quality.

You will find attached the current packaging design of the product. what we do not like:
- The design is not modern
- The design does not evoke the purpose of the product

You will also find attached the logo of our company.

Ps : You can change the color of the logo

Font styles to use
Serif
Sans Serif

Colors

Designer to choose colors to be used in the design.

Requirements
Must have
• - Bottle and box packaging required.
• - Product is bottle of 30 tablets
Should not have
• Sales and other "must buy" "guaranteed" etc

```html
<!DOCTYPE html>
<html lang="fr">
<head>
<meta charset="utf-8">
<title>Velomira – Norvabien</title>
<link href="https://fonts.googleapis.com/css2?family=Oswald:wght@400;700&family=Roboto+Condensed:wght@400;700&display=swap" rel="stylesheet">
<style>
  :root{
    --green:#2fe01e;
    --green-dark:#1fb814;
    --ink:#141414;
    --paper:#f4f4f2;
    --paper-shade:#e9e9e7;
    --white:#ffffff;
  }
  *{margin:0;padding:0;box-sizing:border-box}
  html,body{width:1200px;height:1027px;overflow:hidden;background:var(--white)}
  .canvas{position:relative;width:1200px;height:1027px;font-family:"Roboto Condensed",sans-serif;color:var(--ink)}

  /* brand name */
  .brand{display:flex;align-items:center;gap:6px;justify-content:center}
  .brand-dot{width:14px;height:14px;border-radius:50%;background:var(--green)}
  .brand-name{font-family:"Oswald",sans-serif;font-weight:700;color:var(--ink);letter-spacing:.5px}
  .brand-tag{font-size:7px;letter-spacing:.6px;text-transform:uppercase;color:#444;text-align:center;margin-top:2px}

  /* box: side panel */
  .box-side{position:absolute;left:85px;top:385px;width:140px;height:612px;
    background:linear-gradient(90deg,var(--green-dark),var(--green));color:var(--ink);padding:48px 12px 0 14px}
  .box-side .brand-name{font-size:19px;color:var(--white)}
  .box-side .brand-dot{background:var(--white);width:10px;height:10px}
  .box-side .brand-tag{color:var(--white);font-size:5px}
  .side-copy{font-size:9.5px;line-height:20px;margin-top:32px;text-align:justify}
  .side-maker{font-size:9.5px;line-height:17px;position:absolute;top:405px;left:14px}
  .side-web{font-size:9.5px;letter-spacing:.5px;position:absolute;top:512px;left:14px}

  /* box: front panel */
  .box-front{position:absolute;left:225px;top:385px;width:372px;height:612px;
    background:linear-gradient(90deg,var(--paper-shade),var(--paper) 20%,var(--white));text-align:center}
  .box-front .brand{margin-top:62px}
  .box-front .brand-name{font-size:30px}

  .product-name{font-family:"Oswald",sans-serif;font-weight:700;line-height:1;color:var(--ink)}
  .box-front .product-name .line1{display:block;font-size:82px;margin-top:68px;letter-spacing:2px}
  .box-front .product-name .line2{display:block;font-size:58px;margin-top:4px;letter-spacing:1px}

  .ingredients{border:1.5px dashed #444;font-family:"Roboto Condensed",sans-serif;font-weight:700;
    text-transform:uppercase;line-height:1.35}
  .box-front .ingredients{width:246px;margin:24px auto 0;padding:6px 4px;font-size:14px}

  .benefits{font-size:15px;line-height:1.2;color:#222}
  .box-front .benefits{margin-top:58px}

  .count-band{background:var(--green);color:var(--white);font-family:"Oswald",sans-serif;font-weight:400;letter-spacing:1px}
  .box-front .count-band{position:absolute;left:48px;right:30px;top:538px;height:76px;font-size:22px;
    padding-top:16px;border-radius:6px 6px 0 0}

  /* bottle */
  .bottle{position:absolute;left:700px;top:372px;width:410px;height:655px;background:#f7f7f7}
  .bottle-cap{position:absolute;left:16px;top:60px;width:336px;height:128px;border-radius:16px 16px 4px 4px;
    background:linear-gradient(180deg,var(--white),var(--paper-shade))}
  .bottle-cap::after{content:"";position:absolute;left:0;right:0;top:52px;height:2px;background:#dcdcda}
  .bottle-body{position:absolute;left:14px;top:188px;width:340px;height:445px;border-radius:4px 4px 14px 14px;
    background:linear-gradient(90deg,var(--paper-shade),var(--white) 45%,var(--paper-shade));text-align:center}
  .bottle-body .brand{margin-top:36px}
  .bottle-body .brand-name{font-size:25px}
  .bottle-body .product-name .line1{display:block;font-size:64px;margin-top:26px;letter-spacing:2px}
  .bottle-body .product-name .line2{display:block;font-size:46px;letter-spacing:1px}
  .bottle-body .ingredients{width:192px;margin:14px auto 0;padding:4px;font-size:11px;font-weight:400}
  .bottle-body .benefits{font-size:12px;margin-top:14px}
  .bottle-body .count-band{position:absolute;left:0;right:0;top:337px;height:42px;font-size:17px;padding-top:7px;
    border-radius:8px 8px 0 0}
</style>
</head>
<body>
<div class="canvas">

  <section class="box-side">
    <div class="brand"><span class="brand-dot"></span><span class="brand-name">NORVABIEN</span></div>
    <div class="brand-tag">Hygiène pharmaceutique et diététique</div>
    <p class="side-copy">PROPERTIES: La digestion nous rend souvent lourd et plus fatigué. Ainsi, on peut se retrouver moins énergique et performant après les repas, et cela peut poser problème surtout dans la vie professionnelle</p>
    <p class="side-copy" style="margin-top:16px">Loremp ipsum dolor sit amet</p>
    <p class="side-maker">Manufactured by:<br>Norvabien, 14 Rue Atlas<br>Casablanca<br>0522481730</p>
    <p class="side-web">WWW.NORVABIEN.COM</p>
  </section>

  <section class="box-front">
    <div class="brand"><span class="brand-dot"></span><span class="brand-name">NORVABIEN</span></div>
    <div class="brand-tag">Hygiène pharmaceutique et diététique</div>
    <h1 class="product-name"><span class="line1">VELO</span><span class="line2">MIRA</span></h1>
    <p class="ingredients">Fenouil - Anis vert-Carvi noir<br>Charbon végétal activé</p>
    <p class="benefits">Facilite le transit<br>Améliore la digestion<br>Effect ventre plat</p>
    <div class="count-band">30 GÉLULES</div>
  </section>

  <section class="bottle">
    <div class="bottle-cap"></div>
    <div class="bottle-body">
      <div class="brand"><span class="brand-dot"></span><span class="brand-name">NORVABIEN</span></div>
      <div class="brand-tag">Hygiène pharmaceutique et diététique</div>
      <h2 class="product-name"><span class="line1">VELO</span><span class="line2">MIRA</span></h2>
      <p class="ingredients">Fenouil - Anis vert-Carvi noir<br>Charbon végétal activé</p>
      <p class="benefits">Facilite le transit<br>Améliore la digestion<br>Effect ventre plat</p>
      <div class="count-band">30 GÉLULES</div>
    </div>
  </section>

</div>
</body>
</html>
```